Icons für Filter
Schnelle Komunikation und toller Kontakt und vorallem tolles Design! Weiter so!
Zielgruppe
Wir erstellen einen Online Marktplatz für den Vertrieb von Biolebensmitteln und Naturkosmetik.
Aufgabenstellung
Um die angebotenen Artikel effizient filtern zu können, werden von uns verschiedene Filter angeboten, aufgeteilt nach den kategorien
Siegel, Allergene, Marke
Für die Allergiefilter benötigen wir Icons, die eine Wort-Bildkombination darstellen. D.h. wir hätten gerne ein Icon, das sowohl das Allergen als Text (z.B. "ohne gluten"), als auch als Bild (hier z.B. eine Getreideähre) darstellt.
Die Icons sollen 40*40px messen.
Das gesamte Design ist sehr flat gestaltet.
Die folgenden Icons werden bnötigt:
- ohne Gluten
- ohne Senf
- ohne Sesam
- ohne Soja
- ohne Milch
- ohne Nüsse
- ohne Sellerie
- ohne Ei
- ohne Erdnüsse
- ohne Weizen
- laktosefrei
- glutenfrei
- histaminarm
- fruktosearm
Der angehängte Screenshot zeigt eine Seite des Marktplatzes. In der linken Spalte im Bereich "Allergene" sollen die zu entwickelnden Icons verwendet werden.
Die Besipielallergiefilter zeigen das Prinzip, nachdem die Icons aufgebaut sein sollten. Wir hätten es aber gerne angepasst an unser CD.
Die Farbtöne unseres Corpoprate Designs sind:
Grün: #506e28
hellgrün: #789b2d
dunkelgrau: #4d4d4d

```html
<!DOCTYPE html>
<html lang="de">
<head>
<meta charset="utf-8">
<title>Filter Allergene und Unverträglichkeiten</title>
<link href="https://fonts.googleapis.com/css2?family=Cabin+Condensed:wght@400;500&display=swap" rel="stylesheet">
<style>
  :root {
    --green: #506e28;
    --light-green: #789b2d;
    --pale-green: #b5c98f;
    --dark-grey: #4d4d4d;
    --row-bg: #e8e8e8;
    --box-border: #9a9a9a;
    --page-bg: #ffffff;
  }
  html, body {
    margin: 0;
    padding: 0;
    width: 1183px;
    height: 1200px;
    overflow: hidden;
    background: var(--page-bg);
    font-family: "Cabin Condensed", "Arial Narrow", sans-serif;
  }
  .canvas {
    position: relative;
    width: 1183px;
    height: 1200px;
  }
  .filter-group {
    position: absolute;
    top: 24px;
    width: 324px;
  }
  .filter-group--allergens { left: 218px; }
  .filter-group--intolerance { left: 642px; }

  .filter-head {
    position: relative;
    height: 64px;
  }
  .filter-title {
    margin: 0;
    position: absolute;
    left: 14px;
    top: 2px;
    font-size: 26px;
    font-weight: 400;
    color: var(--green);
    letter-spacing: -0.2px;
  }
  .filter-group--intolerance .filter-title { left: 16px; }
  .filter-caret {
    position: absolute;
    right: 14px;
    top: 16px;
    width: 16px;
    height: 12px;
  }
  .filter-pointer {
    position: absolute;
    left: 150px;
    bottom: 0;
    width: 0;
    height: 0;
    border-left: 12px solid transparent;
    border-right: 12px solid transparent;
    border-bottom: 14px solid var(--row-bg);
  }
  .filter-group--intolerance .filter-pointer { left: 152px; }

  .filter-list {
    list-style: none;
    margin: 17px 0 0;
    padding: 0;
    display: flex;
    flex-direction: column;
    gap: 5px;
  }
  .filter-item {
    position: relative;
    height: 40.6px;
    background: var(--row-bg);
    display: flex;
    align-items: center;
  }
  .filter-icon {
    position: absolute;
    left: 14px;
    top: 5px;
    width: 32px;
    height: 30px;
    border-radius: 6px;
    background: var(--light-green);
  }
  .filter-icon--soft { background: var(--pale-green); }
  .filter-label {
    position: absolute;
    left: 86px;
    font-size: 21px;
    color: var(--dark-grey);
  }
  .filter-label--italic { font-style: italic; }
  .filter-check {
    position: absolute;
    left: 279px;
    top: 10px;
    width: 18px;
    height: 18px;
    margin: 0;
    border: 1px solid var(--box-border);
    background: linear-gradient(#ffffff, #e4e4e4);
    border-radius: 2px;
    appearance: none;
  }
</style>
</head>
<body>
<main class="canvas">

  <section class="filter-group filter-group--allergens">
    <header class="filter-head">
      <h2 class="filter-title">ohne folgende Allergene</h2>
      <svg class="filter-caret" viewBox="0 0 16 12" aria-hidden="true"><path d="M2 10 L8 3 L14 10" fill="none" stroke="#4d4d4d" stroke-width="2.6"/></svg>
      <span class="filter-pointer"></span>
    </header>
    <ul class="filter-list">
      <li class="filter-item"><span class="filter-icon" role="img" aria-label="Icon Getreideähre"></span><span class="filter-label">Gluten</span><input class="filter-check" type="checkbox"></li>
      <li class="filter-item"><span class="filter-icon" role="img" aria-label="Icon Krebs"></span><span class="filter-label">Krebstiere</span><input class="filter-check" type="checkbox"></li>
      <li class="filter-item"><span class="filter-icon" role="img" aria-label="Icon Muschel"></span><span class="filter-label">Weichtiere</span><input class="filter-check" type="checkbox"></li>
      <li class="filter-item"><span class="filter-icon" role="img" aria-label="Icon Senfschote"></span><span class="filter-label">Senf</span><input class="filter-check" type="checkbox"></li>
      <li class="filter-item"><span class="filter-icon" role="img" aria-label="Icon Sesamsamen"></span><span class="filter-label">Sesam</span><input class="filter-check" type="checkbox"></li>
      <li class="filter-item"><span class="filter-icon" role="img" aria-label="Icon Sojabohnen"></span><span class="filter-label">Soja</span><input class="filter-check" type="checkbox"></li>
      <li class="filter-item"><span class="filter-icon" role="img" aria-label="Icon Milchtüte"></span><span class="filter-label">Milch</span><input class="filter-check" type="checkbox"></li>
      <li class="filter-item"><span class="filter-icon" role="img" aria-label="Icon Haselnuss"></span><span class="filter-label">Schalenfrüchte</span><input class="filter-check" type="checkbox"></li>
      <li class="filter-item"><span class="filter-icon" role="img" aria-label="Icon Sellerieblatt"></span><span class="filter-label">Sellerie</span><input class="filter-check" type="checkbox"></li>
      <li class="filter-item"><span class="filter-icon" role="img" aria-label="Icon Lupinenpflanze"></span><span class="filter-label">Lupine</span><input class="filter-check" type="checkbox"></li>
      <li class="filter-item"><span class="filter-icon" role="img" aria-label="Icon Sulfit-Strukturformel"></span><span class="filter-label">Sulfite</span><input class="filter-check" type="checkbox"></li>
      <li class="filter-item"><span class="filter-icon" role="img" aria-label="Icon Fisch"></span><span class="filter-label">Fisch</span><input class="filter-check" type="checkbox"></li>
      <li class="filter-item"><span class="filter-icon" role="img" aria-label="Icon Ei"></span><span class="filter-label">Eier</span><input class="filter-check" type="checkbox"></li>
      <li class="filter-item"><span class="filter-icon" role="img" aria-label="Icon Erdnuss"></span><span class="filter-label">Erdnüsse</span><input class="filter-check" type="checkbox"></li>
      <li class="filter-item"><span class="filter-icon" role="img" aria-label="Icon Weizenähre"></span><span class="filter-label">Weizen</span><input class="filter-check" type="checkbox"></li>
      <li class="filter-item"><span class="filter-icon" role="img" aria-label="Icon Hefegebäck"></span><span class="filter-label">Hefe</span><input class="filter-check" type="checkbox"></li>
    </ul>
  </section>

  <section class="filter-group filter-group--intolerance">
    <header class="filter-head">
      <h2 class="filter-title">Unverträglichkeit auf</h2>
      <svg class="filter-caret" viewBox="0 0 16 12" aria-hidden="true"><path d="M2 10 L8 3 L14 10" fill="none" stroke="#4d4d4d" stroke-width="2.6"/></svg>
      <span class="filter-pointer"></span>
    </header>
    <ul class="filter-list">
      <li class="filter-item"><span class="filter-icon" role="img" aria-label="Icon Histamin-Molekül"></span><span class="filter-label">Histamin frei</span><input class="filter-check" type="checkbox"></li>
      <li class="filter-item"><span class="filter-icon filter-icon--soft" role="img" aria-label="Icon Histamin-Molekül hell"></span><span class="filter-label filter-label--italic">Histamin arm</span><input class="filter-check" type="checkbox"></li>
      <li class="filter-item"><span class="filter-icon" role="img" aria-label="Icon Käse"></span><span class="filter-label">Lactosefrei</span><input class="filter-check" type="checkbox"></li>
      <li class="filter-item"><span class="filter-icon" role="img" aria-label="Icon Obst"></span><span class="filter-label">Fruktose frei</span><input class="filter-check" type="checkbox"></li>
      <li class="filter-item"><span class="filter-icon filter-icon--soft" role="img" aria-label="Icon Obst hell"></span><span class="filter-label">Fruktose arm</span><input class="filter-check" type="checkbox"></li>
      <li class="filter-item"><span class="filter-icon" role="img" aria-label="Icon Zuckerrübe"></span><span class="filter-label">Zuckerfrei</span><input class="filter-check" type="checkbox"></li>
    </ul>
  </section>

</main>
</body>
</html>
```